Retail Jewelry Business Card Design Project

We are in need of a new business card design for a retail jewelry store. This store is in the business of fine jewelry including but not specific to bridal jewelry, diamonds, designer jewelry and watches.

This store has been in business for 20 years but continues to strive for a modern professional appeal. The main colors use for this business are a royal blue, white and silver.

Target Market(s)

Target market is ages 18-50

Industry/Entity Type

Jewelry

Requirements
Must have
• Sales Person Name
Sales Person Email Address

Store Address
Store Phone
Website

Standard business card size. No odd shapes or sizes.
Nice to have
• Overall modern feel for card.

We have thought that a design with a nice feature of the logo on the back of the card would be nice but open to ideas.
Should not have
• No specific images of jewelry should be used.

```html
<!DOCTYPE html>
<html lang="en">
<head>
<meta charset="utf-8">
<title>Marlow Reed Fine Jewelry – Business Cards</title>
<link href="https://fonts.googleapis.com/css2?family=Arimo:wght@400&display=swap" rel="stylesheet">
<style>
  :root {
    --backdrop: #e6e6ea;
    --royal-blue: #2f2b9c;
    --royal-blue-deep: #221e80;
    --card-white: #fbfbfd;
    --silver: #9a9aa6;
    --silver-dark: #7c7c88;
  }
  * { margin: 0; padding: 0; box-sizing: border-box; }
  html, body {
    width: 1200px;
    height: 1000px;
    overflow: hidden;
    background: var(--backdrop);
    font-family: "Arimo", Arial, sans-serif;
  }
  .sheet {
    position: relative;
    width: 1200px;
    height: 1000px;
  }
  .card {
    position: absolute;
    left: 280px;
    width: 640px;
    height: 366px;
    border-radius: 4px;
    box-shadow: 0 6px 20px rgba(0, 0, 0, 0.18);
    overflow: hidden;
  }
  /* Contact side */
  .card--contact {
    top: 110px;
    background: linear-gradient(135deg, #ffffff 0%, var(--card-white) 60%, #ececf2 100%);
  }
  .contact-list {
    position: absolute;
    left: 48px;
    top: 52px;
    list-style: none;
    color: var(--silver-dark);
    font-size: 17px;
    line-height: 1.25;
  }
  .contact-list li { margin-bottom: 16px; }
  .contact-list .gap { margin-top: 22px; }
  .contact-list .tight { margin-bottom: 4px; }
  .brand--contact {
    position: absolute;
    right: 44px;
    bottom: 44px;
    text-align: center;
    color: var(--silver);
  }
  /* Brand side */
  .card--brand {
    top: 524px;
    background: radial-gradient(ellipse at 60% 35%, #3833ad 0%, var(--royal-blue) 55%, #28248c 100%);
  }
  .brand--front {
    position: absolute;
    left: 52px;
    bottom: 56px;
    text-align: center;
    color: var(--royal-blue-deep);
  }
  .brand-name {
    font-size: 44px;
    line-height: 1;
    letter-spacing: 0.5px;
  }
  .brand-rule {
    display: block;
    height: 2px;
    margin: 8px 0 6px;
    background: currentColor;
  }
  .brand-tag {
    font-size: 20px;
    letter-spacing: 4px;
  }
  .brand--contact .brand-name { font-size: 30px; }
  .brand--contact .brand-tag { font-size: 13px; letter-spacing: 3px; }
  .brand--contact .brand-rule { height: 1px; margin: 6px 0 4px; }
</style>
</head>
<body>
  <main class="sheet">
    <section class="card card--contact" aria-label="Business card contact side">
      <ul class="contact-list">
        <li>Marlow Reed Halvorsen</li>
        <li>marlow@marlowreedjewelry.com</li>
        <li>0455 128 604</li>
        <li class="gap tight">2280 Linden Avenue</li>
        <li class="tight">Bayport City, FL 30512</li>
        <li>www.marlowreedjewelry.com</li>
      </ul>
      <div class="brand brand--contact">
        <div class="brand-name">Marlow Reed</div>
        <span class="brand-rule"></span>
        <div class="brand-tag">FINE JEWELRY</div>
      </div>
    </section>

    <section class="card card--brand" aria-label="Business card brand side">
      <div class="brand brand--front">
        <div class="brand-name">Marlow Reed</div>
        <span class="brand-rule"></span>
        <div class="brand-tag">FINE JEWELRY</div>
      </div>
    </section>
  </main>
</body>
</html>
```